Professional DJ Business Card

Business card for giving out to clubs and venues or interested groups that are in need of a professional DJ. I want something artistic and catchy/alluring, with a minimalist approach that gets just the vital amount of info and leaves the rest for inquiry via contacting me. Ideally I would like one side to have an image of something cool like an eye and my name, then the other side be the contact info, I am definitely feeling a black or dark colored card, but I am open to other designs. I am uploading a picture that I made that reflects a little of what I am *kind of* looking for.

Industry/Entity Type

Business

Contact Information for Business Card

Tomas Halvik (Voxtel)
Professional DJ (West Coast)
EDM (Deep/House/Techno), Hip Hop, Latin, Trap.
Cell: 555-274-9163
Email: Voxtelofficial@mailnest.net
www.beatcloudia.net/yourtuneisfading

```html
<!DOCTYPE html>
<html lang="en">
<head>
<meta charset="utf-8">
<title>Voxtel – Professional DJ Business Card</title>
<link href="https://fonts.googleapis.com/css2?family=Open+Sans:wght@400;600;700&family=Pinyon+Script&display=swap" rel="stylesheet">
<style>
  :root {
    --backdrop: #efe3cc;
    --card-dark: #111210;
    --card-light: #ffffff;
    --ink-light: #ffffff;
    --ink-dark: #111111;
    --art-glow: rgba(235, 235, 235, 0.22);
    --art-fade: rgba(235, 235, 235, 0);
    --shadow: rgba(60, 45, 20, 0.45);
  }
  * { margin: 0; padding: 0; box-sizing: border-box; }
  html, body {
    width: 1189px;
    height: 1200px;
    overflow: hidden;
    background: var(--backdrop);
    font-family: "Open Sans", Arial, sans-serif;
  }
  .canvas {
    position: relative;
    width: 1189px;
    height: 1200px;
  }
  .card {
    position: absolute;
    left: 183px;
    width: 833px;
    height: 488px;
    box-shadow: 6px 8px 10px var(--shadow);
    text-align: center;
  }
  .card--front {
    top: 68px;
    background: var(--card-dark);
    color: var(--ink-light);
  }
  .card--back {
    top: 626px;
    background: var(--card-light);
    color: var(--ink-dark);
  }
  .front__artwork {
    position: absolute;
    left: 300px;
    top: 40px;
    width: 450px;
    height: 160px;
    border-radius: 50%;
    background: radial-gradient(ellipse at center, var(--art-glow) 0%, var(--art-fade) 70%);
  }
  .brand__name {
    position: absolute;
    left: 0;
    right: 0;
    top: 196px;
    font-size: 100px;
    font-weight: 600;
    line-height: 1;
    color: var(--ink-light);
  }
  .front__url {
    position: absolute;
    left: 0;
    right: 0;
    top: 404px;
    font-size: 21px;
    color: var(--ink-light);
  }
  .back__name {
    position: absolute;
    left: 0;
    right: 0;
    top: 76px;
    font-family: "Pinyon Script", cursive;
    font-weight: 400;
    font-size: 60px;
    line-height: 1.2;
  }
  .back__role {
    position: absolute;
    left: 0; right: 0;
    top: 155px;
    font-size: 23px;
  }
  .back__genres {
    position: absolute;
    left: 0; right: 0;
    top: 198px;
    font-size: 19.5px;
  }
  .back__contact {
    position: absolute;
    left: 0; right: 0;
    top: 284px;
    font-size: 22px;
    line-height: 34px;
  }
  .back__contact b { font-weight: 700; }
  .back__url {
    position: absolute;
    left: 0; right: 0;
    top: 368px;
    font-size: 21.5px;
    font-weight: 600;
  }
</style>
</head>
<body>
<main class="canvas">
  <section class="card card--front" aria-label="Card front">
    <div class="front__artwork" role="img" aria-label="Area for the artist's sketched eye artwork in white on black"></div>
    <p class="brand__name">Voxtel</p>
    <p class="front__url">www.beatcloudia.net/yourtuneisfading</p>
  </section>

  <section class="card card--back" aria-label="Card back">
    <h1 class="back__name">Tomas Halvik (Voxtel)</h1>
    <p class="back__role">Professional DJ (West Coast)</p>
    <p class="back__genres">EDM (Deep/House/Techno), Hip Hop, Latin, Trap.</p>
    <p class="back__contact">
      <b>Cell:</b> 555-274-9163<br>
      <b>Email:</b> Voxtelofficial@mailnest.net
    </p>
    <p class="back__url">www.beatcloudia.net/yourtuneisfading</p>
  </section>
</main>
</body>
</html>
```